Business Card / Thank You Card for Little Girl Website

This is a company that will be designing do it yourself kits for doll furniture in addition to little girl apparel featuring our logo. The name of the company is Wander the Meadow. The website is written as www.wander the meadow.com with hearts dotting the i's. It's meant to be a website to inspire girls to be creative. We will be using a lower case scripted I dotted with a heart as our logo. Any thoughts? Light Pink, purple and silver are the colors we've chosen. The card is going to be going in each kit as a "Thank you" from Posy so it's not your traditional business card. We can do something along the lines of "I hope I've inspired you! Your friend, Posy!" and dot the i's in inspired with hearts? And then put the website address below it. The font for the website is Wander the Meadow - Jenna Sue www.wanderthemeadow.com - Flirty Girl (hearts dotting the i's on this line only) I'm open to suggestions for something different!
Target Market(s)
Young girls ages 5-10
Industry/Entity Type
Business
Contact Information for Business Card
Laurie Casalelauriecasale@hotmail.com9788360085
Font styles to use
Other font styles liked:
- Jenna Sue and Flirty Girl
Requirements
Must have
- Pinks and Purples
Nice to have
- A cute design for Little Girls. Something fun and whimsical.

```html
<!DOCTYPE html>
<html lang="en">
<head>
<meta charset="utf-8">
<title>Wander the Meadow – Card Presentation</title>
<link rel="stylesheet" href="https://fonts.googleapis.com/css2?family=Caveat:wght@400;500&family=Sorts+Mill+Goudy&family=Arimo:wght@700&display=swap">
<style>
  :root {
    --paper: #ffffff;
    --brand-pink: #e0409a;
    --card-pink: #e2479d;
    --card-pink-light: #ec74b6;
    --on-card: #ffffff;
    --trim-red: #e42b2b;
    --safe-blue: #27b3e6;
    --ink: #111111;
  }
  * { margin: 0; padding: 0; box-sizing: border-box; }
  html, body { width: 927px; height: 1200px; overflow: hidden; background: var(--paper); }
  .sheet { position: relative; width: 927px; height: 1200px; }

  .brand-title {
    position: absolute; left: 0; top: 104px; width: 927px;
    text-align: center; white-space: nowrap;
    font-family: "Caveat", cursive;
    font-weight: 400; font-size: 112px; line-height: 1.2;
    color: var(--brand-pink);
  }

  .side-label {
    position: absolute; left: 90px;
    font-family: "Sorts Mill Goudy", Georgia, serif;
    font-size: 42px; color: var(--ink);
  }
  .side-label--front { top: 418px; }
  .side-label--back  { top: 710px; }

  .card {
    position: absolute; left: 272px; width: 402px; height: 235px;
    font-family: "Caveat", cursive; color: var(--on-card);
  }
  .card--front { top: 326px; }
  .card--back  { top: 618px; }

  .card__pattern {
    position: absolute; inset: 0;
    background: radial-gradient(ellipse at 50% 50%, var(--card-pink-light) 0%, var(--card-pink) 75%);
  }
  .card__trim  { position: absolute; inset: 8px;  border: 1.5px solid var(--trim-red); }
  .card__safe  { position: absolute; inset: 13px; border: 1.5px solid var(--safe-blue); }

  .card__name {
    position: absolute; left: 0; right: 0; top: 82px;
    text-align: center; white-space: nowrap;
    font-size: 48px; line-height: 1;
  }
  .card__url {
    position: absolute; left: 0; right: 0; top: 168px;
    text-align: center; white-space: nowrap;
    font-size: 18px; font-weight: 500; line-height: 1;
  }

  .card__message { position: absolute; font-size: 36px; line-height: 1; white-space: nowrap; }
  .card__message--one { left: 34px; top: 44px; }
  .card__message--two { left: 62px; top: 78px; }
  .card__signoff { position: absolute; left: 242px; top: 136px; font-size: 22px; white-space: nowrap; }
  .card__signature {
    position: absolute; left: 262px; top: 160px;
    font-size: 36px; display: flex; align-items: center; gap: 3px; white-space: nowrap;
  }

  .spec {
    position: absolute; left: 278px; top: 896px; width: 388px; height: 219px;
    border: 1.5px solid var(--trim-red);
    font-family: "Arimo", Arial, sans-serif; font-weight: 700; color: var(--ink);
  }
  .spec__safe { position: absolute; inset: 5px; border: 1.5px solid var(--safe-blue); }
  .spec__row { position: absolute; left: 58px; display: flex; align-items: center; }
  .spec__row--trim { top: 15px; }
  .spec__row--safe { top: 43px; }
  .spec__tag {
    width: 191px; height: 22px; border: 1.5px solid var(--ink);
    font-size: 12px; text-align: right; padding-right: 8px; line-height: 19px;
  }
  .spec__swatch { margin-left: 14px; width: 68px; height: 4px; }
  .spec__swatch--trim { background: var(--trim-red); }
  .spec__swatch--safe { background: var(--safe-blue); }
  .spec__notes {
    position: absolute; left: 146px; top: 74px;
    font-size: 10px; word-spacing: 4px;
  }
  .spec__notes span { margin-left: 18px; }
</style>
</head>
<body>
<main class="sheet">
  <h1 class="brand-title">Wander the Meadow</h1>

  <p class="side-label side-label--front">Front</p>
  <section class="card card--front">
    <div class="card__pattern" role="img" aria-label="Pink background with soft lighter floral vine pattern"></div>
    <div class="card__trim"></div>
    <div class="card__safe"></div>
    <p class="card__name">Wander the Meadow</p>
    <p class="card__url">www.wanderthemeadow.com</p>
  </section>

  <p class="side-label side-label--back">Back</p>
  <section class="card card--back">
    <div class="card__pattern" role="img" aria-label="Pink background with soft lighter floral vine pattern"></div>
    <div class="card__trim"></div>
    <div class="card__safe"></div>
    <p class="card__message card__message--one">I'm excited to see</p>
    <p class="card__message card__message--two">how you will be inspired!</p>
    <p class="card__signoff">Your friend,</p>
    <p class="card__signature">
      <svg width="20" height="18" viewBox="0 0 20 18" aria-hidden="true">
        <path d="M10 16 C3 11 1 8 1 5.5 A4 4 0 0 1 10 4 A4 4 0 0 1 19 5.5 C19 8 17 11 10 16 Z" fill="none" stroke="#ffffff" stroke-width="1.6"/>
      </svg>
      Posy
    </p>
  </section>

  <section class="spec">
    <div class="spec__safe"></div>
    <div class="spec__row spec__row--trim">
      <div class="spec__tag">TRIM</div>
      <div class="spec__swatch spec__swatch--trim"></div>
    </div>
    <div class="spec__row spec__row--safe">
      <div class="spec__tag">SAFE MARGIN</div>
      <div class="spec__swatch spec__swatch--safe"></div>
    </div>
    <p class="spec__notes">CMYK<span>300 DPI</span></p>
  </section>
</main>
</body>
</html>
```